Thornwick Estates Managment Ltd website

Need a website To inform people/clients of the services we provide. 5 pages total with a local feel. Bristol, UK. I have logo artwork already is like the look based on
incorporate the artwork attached for theme, feel and colours fonts info etc

To best describe the business have a brief look at www.fernbaylettings.co.uk which is a local firm offering the same services. This is for your ref only and not to be copied.

Target Market(s)

Property Investors/Landlords

Coding

Coded - Design and coding required

Number of Pages Required

5+ page

Colors
0392cd
f68d4d

Requirements
Must have
• local feel. Possibly using some local architecture or historic landmarks etc. This is fexible.
• most also be mobile device compatible
Nice to have
• the membership logos - files attached: KTB, GHW, DVT and safebondhold.co.uk

```html
<!DOCTYPE html>
<html lang="en">
<head>
<meta charset="utf-8">
<title>Thornwick Estates Managment Ltd</title>
<link rel="stylesheet" href="https://fonts.googleapis.com/css2?family=Maven+Pro:wght@400;500;700&family=Lato:wght@400;700&display=swap">
<style>
:root{
  --blue:#0392cd;
  --blue-dark:#0a6fa0;
  --navy:#174a6b;
  --swoosh:#0e5a86;
  --orange:#f68d4d;
  --ink:#222;
  --text:#444;
  --grey-band:#ececec;
  --line:#cfcfcf;
  --white:#fff;
  --footer-bar:#2b2b2b;
}
*{box-sizing:border-box;margin:0;padding:0}
html,body{width:675px;height:1200px;overflow:hidden;background:var(--white)}
body{position:relative;font-family:'Lato',sans-serif;color:var(--text)}
.abs{position:absolute}
.heading{font-family:'Maven Pro',sans-serif}

/* header */
.site-header{left:0;top:0;width:675px;height:66px;background:var(--white);border-bottom:1px solid #e4e4e4}
.phone-tab{left:504px;top:0;width:116px;height:20px;background:var(--blue);color:var(--white);font-size:8.5px;font-weight:700;display:flex;align-items:center;justify-content:center;gap:5px;clip-path:polygon(0 0,100% 0,93% 100%,7% 100%)}
.brand{left:60px;top:18px;display:flex;align-items:center;gap:6px}
.brand-square{width:22px;height:22px;background:var(--blue)}
.brand-name{font-family:'Maven Pro',sans-serif;font-weight:700;font-size:16px;color:var(--navy);line-height:1}
.brand-sub{font-family:'Maven Pro',sans-serif;font-weight:700;font-size:7px;color:var(--navy);line-height:1.2}
.main-nav{left:224px;top:38px;display:flex;font-size:9.5px;color:#444;text-transform:uppercase}
.main-nav a{color:inherit;text-decoration:none;padding:0 14px;border-left:1px solid #ccc;line-height:12px}
.main-nav a:first-child{padding-left:0;border-left:none;color:var(--blue);border-bottom:2px solid var(--blue);padding-bottom:4px}

/* hero */
.hero{left:0;top:66px;width:675px;height:262px;
  background:
    radial-gradient(ellipse 60% 55% at 88% 10%,rgba(58,112,190,.95),rgba(58,112,190,0) 70%),
    linear-gradient(100deg,#b9a382 0%,#9c8462 30%,#7d6649 55%,#5d4c3a 75%,#3e3429 100%)}
.hero-title{right:56px;top:128px;text-align:right;font-family:'Maven Pro',sans-serif;font-weight:500;font-size:23px;line-height:30px;color:var(--white);text-shadow:0 1px 3px rgba(0,0,0,.5)}
.hero-sub{right:56px;top:196px;text-align:right;font-size:11px;line-height:15.5px;color:var(--white);text-shadow:0 1px 3px rgba(0,0,0,.6)}
.hero-dots{right:56px;top:251px;display:flex;gap:3px}
.hero-dots span{width:7px;height:7px;border-radius:50%;border:1px solid #ddd}
.hero-dots span.on{background:var(--blue);border-color:#fff}

/* welcome */
.welcome-kicker{left:56px;top:345px;font-size:15px;color:#333}
.welcome-title{left:56px;top:366px;font-weight:500;font-size:20.5px;color:var(--blue)}
.welcome-rule{left:56px;top:394px;width:360px;height:1px;background:var(--line)}
.welcome-lead{left:56px;top:400px;width:360px;font-weight:700;font-size:10px;line-height:14px;color:var(--ink)}
.welcome-body{left:56px;top:431px;width:365px;font-size:7.6px;line-height:14.4px;color:#444}
.btn{display:flex;align-items:center;height:17px;background:linear-gradient(#2c82a8,#155a7c);color:var(--white);font-family:'Maven Pro',sans-serif;font-weight:500;font-size:9.5px;padding:0 6px 0 4px;gap:5px;white-space:nowrap}
.btn-mark{width:12px;height:12px;background:var(--white);opacity:.9}
.welcome-btn{left:58px;top:494px}

/* contact form */
.contact-box{left:441px;top:342px;width:178px;height:175px;background:#f7f7f7;border:1px solid #ddd;box-shadow:0 1px 3px rgba(0,0,0,.15)}
.contact-head{height:34px;background:var(--blue);color:var(--white);font-family:'Maven Pro',sans-serif;font-weight:500;font-size:14px;display:flex;align-items:center;justify-content:center;letter-spacing:.5px}
.field{position:absolute;left:10px;width:158px;height:17px;background:var(--white);border:1px solid #ccc;font-size:6.5px;color:#777;padding:4px 5px;font-style:italic}
.submit-btn{position:absolute;left:11px;top:148px}

/* services */
.services{left:0;top:540px;width:675px;height:252px;background:var(--grey-band)}
.card{top:556px;width:175px;height:215px;background:var(--white);border:1px solid #dcdcdc;box-shadow:0 1px 2px rgba(0,0,0,.08)}
.card-head{position:absolute;left:5px;top:5px;width:164px;height:24px;background:var(--blue);color:var(--white);font-family:'Maven Pro',sans-serif;font-weight:500;font-size:11px;display:flex;align-items:center;justify-content:center;gap:8px}
.card-photo{position:absolute;left:5px;top:33px;width:164px;height:105px}
.photo-keys{background:radial-gradient(ellipse 55% 60% at 40% 55%,#d8b898,rgba(216,184,152,0) 70%),linear-gradient(110deg,#f2efec 0%,#8b6a52 45%,#2f2a27 100%)}
.photo-tenants{background:radial-gradient(ellipse 60% 50% at 60% 70%,#dfe7ef,rgba(223,231,239,0) 70%),linear-gradient(120deg,#f4f6f8 0%,#b9c6d3 45%,#6e7b88 100%)}
.photo-team{background:radial-gradient(ellipse 70% 55% at 50% 75%,#d7dde6,rgba(215,221,230,0) 70%),linear-gradient(180deg,#fafafa 0%,#ece9e5 45%,#8a8a8e 100%)}
.card-text{position:absolute;left:10px;top:147px;width:154px;text-align:center;font-size:6.8px;line-height:10.5px;color:#444}
.card .btn{position:absolute;left:45px;top:185px}

/* affiliates */
.affiliates-title{left:0;top:810px;width:675px;text-align:center;font-weight:500;font-size:16px;color:var(--blue)}
.affiliates-rule{left:268px;top:836px;width:139px;height:1px;background:var(--line)}
.aff-box{top:866px;width:128px;height:72px;background:var(--white);border:1px solid #c8c8c8;display:flex;align-items:center;justify-content:center}
.aff-box.active{border:2px solid var(--blue)}
.aff-arrow{top:894px;width:15px;height:15px}

/* footer */
.footer-wave{left:0;top:940px;width:675px;height:236px}
.newsletter-input{left:77px;top:1028px;width:107px;height:14px;background:var(--white);border:1px solid #bbb;font-size:6px;font-style:italic;color:#777;padding:3px 4px}
.newsletter-btn{left:186px;top:1028px;width:56px;height:14px;background:var(--orange);color:var(--white);font-size:6.5px;font-weight:700;display:flex;align-items:center;justify-content:center;letter-spacing:.5px}
.foot-col{top:1066px;color:var(--white)}
.foot-col h3{font-family:'Maven Pro',sans-serif;font-weight:500;font-size:11px;padding-bottom:4px;border-bottom:1px solid rgba(255,255,255,.35);margin-bottom:6px;width:62px;white-space:nowrap}
.quick-links li{list-style:none;font-size:7.6px;line-height:12.3px}
.contact-details{font-size:7px;line-height:9.6px}
.contact-row{display:flex;gap:8px;margin-bottom:8px}
.contact-row svg{flex:none;margin-top:1px}
.col-sep{top:1066px;width:1px;height:100px;background:rgba(255,255,255,.25)}
.map-area{position:absolute;left:0;top:25px;width:153px;height:64px;background:linear-gradient(135deg,#dfe3d6,#e9ecdf 50%,#cfdcc5);border:2px solid var(--white)}
.view-location{position:absolute;left:6px;top:93px;font-size:6px;white-space:nowrap}
.social-row{display:flex;align-items:center;gap:8px;font-size:7.6px;height:20px;margin-bottom:5px}
.social-dot{width:16px;height:16px;border-radius:50%;border:1.5px solid var(--white)}
.footer-bar{left:0;top:1176px;width:675px;height:24px;background:var(--footer-bar);color:#ddd;font-size:7px;display:flex;align-items:center;justify-content:center}
</style>
</head>
<body>

<header class="site-header abs">
  <div class="phone-tab abs">
    <svg width="9" height="9" viewBox="0 0 10 10"><circle cx="5" cy="5" r="4.4" fill="none" stroke="#fff" stroke-width="1"/><path d="M3.4 2.8c.3-.3.6-.2.8.1l.4.7c.1.2 0 .4-.2.6l-.2.2c.3.6.7 1 1.3 1.3l.2-.2c.2-.2.4-.2.6-.1l.7.4c.3.2.4.5.1.8-.5.5-1.2.6-2 .1-.9-.6-1.6-1.3-2-2.2-.3-.7-.2-1.3.3-1.7z" fill="#fff"/></svg>
    07700 900461
  </div>
  <div class="brand abs">
    <div class="brand-square"></div>
    <div>
      <div class="brand-name">Thornwick</div>
      <div class="brand-sub">estates management ltd</div>
    </div>
  </div>
  <nav class="main-nav abs">
    <a href="#">Home</a><a href="#">About Us</a><a href="#">Landlords</a><a href="#">Agencies</a><a href="#">Projects</a><a href="#">Contact</a>
  </nav>
</header>

<section class="hero abs" role="img" aria-label="Photograph of historic Bristol stone buildings and a gothic tower under a blue sky"></section>
<h1 class="hero-title abs">Thornwick Estate<br>Management</h1>
<p class="hero-sub abs">THE PERFECT SOLUTION FOR<br>LANDLORDS, TENANTS &amp; AGENCIES<br>IN BRISTOL</p>
<div class="hero-dots abs"><span></span><span class="on"></span><span></span><span></span></div>

<p class="welcome-kicker abs heading">Welcome to</p>
<h2 class="welcome-title abs heading">Thornwick Estates Mgmt Ltd</h2>
<div class="welcome-rule abs"></div>
<p class="welcome-lead abs">Ut wisi enim ad minim veniam, quis nostrud exercimol tation ullamcorper suscipit lobortis nisl ut aliquip ex ea.</p>
<p class="welcome-body abs">Lorem ipsum dolor sit amet, consectetuer adipiscing elit, sed diam nonummy nibh euism tinciduntl ut laoreet dolore maex ea commodo consequat. Duis autem v eummu iriure dolor in hendrerit in vulputate velit esse molestie consequat, vel illum dolore eu feugi nullaml facilisis at vero eros et accumsan et iusto facilisi ate velit esse molestie consequat.</p>
<a class="btn welcome-btn abs"><span class="btn-mark"></span>Learn More</a>

<aside class="contact-box abs">
  <div class="contact-head">CONTACT US</div>
  <div class="field" style="top:44px">Name</div>
  <div class="field" style="top:66px">Email</div>
  <div class="field" style="top:87px">Phone</div>
  <div class="field" style="top:109px;height:33px">Message</div>
  <a class="btn submit-btn"><span class="btn-mark"></span>Submit</a>
</aside>

<section class="services abs"></section>

<article class="card abs" style="left:55px">
  <div class="card-head">
    <svg width="12" height="12" viewBox="0 0 12 12" fill="#fff"><circle cx="6" cy="3.5" r="2.5"/><path d="M1 12c0-3 2.2-5 5-5s5 2 5 5z"/></svg>FOR LANDLORDS
  </div>
  <div class="card-photo photo-keys" role="img" aria-label="Photograph of a hand passing house keys"></div>
  <p class="card-text">Lorem ipsum dolor sit amet, consectetuer adipiscing elit, sed diam nonummy nibh euism tinciduntl ut laoreet dolore maex</p>
  <a class="btn"><span class="btn-mark"></span>Learn More</a>
</article>

<article class="card abs" style="left:250px">
  <div class="card-head">
    <svg width="16" height="12" viewBox="0 0 16 12" fill="#fff"><circle cx="5" cy="3.5" r="2.3"/><circle cx="11" cy="3.5" r="2.3"/><path d="M0 12c0-3 2-4.8 5-4.8s5 1.8 5 4.8zM6 12c0-3 2-4.8 5-4.8s5 1.8 5 4.8z"/></svg>FOR TENANTS
  </div>
  <div class="card-photo photo-tenants" role="img" aria-label="Photograph of tenants shaking hands across a table"></div>
  <p class="card-text">Lorem ipsum dolor sit amet, consectetuer adipiscing elit, sed diam nonummy nibh euism tinciduntl ut laoreet dolore maex</p>
  <a class="btn"><span class="btn-mark"></span>Learn More</a>
</article>

<article class="card abs" style="left:446px">
  <div class="card-head">
    <svg width="16" height="13" viewBox="0 0 16 13" fill="none" stroke="#fff" stroke-width="1.2"><rect x="2" y="3" width="12" height="9"/><path d="M5 3V1h6v2M2 7h12"/></svg>FOR AGENCIES
  </div>
  <div class="card-photo photo-team" role="img" aria-label="Photograph of a team of agency staff"></div>
  <p class="card-text">Lorem ipsum dolor sit amet, consectetuer adipiscing elit, sed diam nonummy nibh euism tinciduntl ut laoreet dolore maex</p>
  <a class="btn"><span class="btn-mark"></span>Learn More</a>
</article>

<h2 class="affiliates-title abs heading">Our Affiliates</h2>
<div class="affiliates-rule abs"></div>

<svg class="aff-arrow abs" style="left:27px" viewBox="0 0 16 16"><circle cx="8" cy="8" r="7" fill="none" stroke="#555" stroke-width="1.3"/><path d="M11.5 8h-7M7.5 5 4.5 8l3 3" fill="none" stroke="#555" stroke-width="1.3"/></svg>
<div class="aff-box abs" style="left:55px" role="img" aria-label="safebondhold.co.uk membership badge"><div style="width:96px;height:16px;border-radius:3px;background:#8e8e8e"></div></div>
<div class="aff-box active abs" style="left:200px" role="img" aria-label="KTB membership badge"><div style="width:40px;height:48px;border-radius:3px;background:#1a9aa8"></div></div>
<div class="aff-box abs" style="left:346px" role="img" aria-label="DVT membership badge"><div style="width:100px;height:28px;border-radius:3px;background:#9c9c9c"></div></div>
<div class="aff-box abs" style="left:491px" role="img" aria-label="GHW membership badge"><div style="width:64px;height:44px;border-radius:3px;background:#2d2d2d"></div></div>
<svg class="aff-arrow abs" style="left:634px" viewBox="0 0 16 16"><circle cx="8" cy="8" r="7" fill="none" stroke="#555" stroke-width="1.3"/><path d="M4.5 8h7M8.5 5l3 3-3 3" fill="none" stroke="#555" stroke-width="1.3"/></svg>

<footer>
  <svg class="footer-wave abs" viewBox="0 0 675 236" preserveAspectRatio="none">
    <path d="M0 100C90 40 210 38 300 72C380 102 470 108 555 84C620 64 655 34 675 0V236H0Z" fill="var(--swoosh)"/>
    <path d="M0 112C95 58 210 54 298 82C380 108 470 112 555 92C620 76 656 46 675 18V236H0Z" fill="var(--white)"/>
    <path d="M0 122C95 68 210 64 298 90C380 114 470 118 555 100C620 86 656 56 675 26V236H0Z" fill="var(--blue)"/>
  </svg>

  <div class="newsletter-input abs">Email Address</div>
  <div class="newsletter-btn abs">SUBSCRIBE</div>

  <div class="foot-col abs" style="left:56px">
    <h3>Quick Links</h3>
    <ul class="quick-links">
      <li>Home</li><li>About Us</li><li>Landlords</li><li>Agencies</li><li>Projects</li><li>Contact Us</li>
    </ul>
  </div>
  <div class="col-sep abs" style="left:141px"></div>

  <div class="foot-col abs" style="left:170px">
    <h3 style="width:120px">Contact Details</h3>
    <div class="contact-details">
      <div class="contact-row"><svg width="7" height="9" viewBox="0 0 8 10"><path d="M4 0a3.4 3.4 0 0 0-3.4 3.4C.6 6 4 10 4 10s3.4-4 3.4-6.6A3.4 3.4 0 0 0 4 0zm0 4.8a1.4 1.4 0 1 1 0-2.8 1.4 1.4 0 0 1 0 2.8z" fill="#fff"/></svg><span>Ashdene House<br>42 Cotham Vale,<br>Bristol, BS6 6HR</span></div>
      <div class="contact-row"><svg width="8" height="8" viewBox="0 0 10 10"><path d="M2 .8c.4-.4.8-.3 1 .1l.7 1.2c.2.3.1.6-.2.8l-.5.4c.5 1 1.2 1.8 2.2 2.3l.4-.5c.2-.3.5-.3.8-.2l1.2.7c.4.2.5.6.1 1-.8.8-1.8 1-3 .4-1.5-.8-2.6-2-3.3-3.5C.9 2.4 1.2 1.5 2 .8z" fill="#fff"/></svg><span>07700 900461</span></div>
      <div class="contact-row"><svg width="8" height="7" viewBox="0 0 10 8"><rect x=".5" y=".5" width="9" height="7" fill="none" stroke="#fff"/><path d="M.5.5 5 4.5 9.5.5" fill="none" stroke="#fff"/></svg><span>hello@thornwickestates.co.uk</span></div>
    </div>
  </div>
  <div class="col-sep abs" style="left:314px"></div>

  <div class="foot-col abs" style="left:342px;width:160px;height:110px">
    <h3 style="width:114px">Location Map</h3>
    <div class="map-area" role="img" aria-label="Street map of the office location in Bristol"></div>
    <span class="view-location">View Location »</span>
  </div>
  <div class="col-sep abs" style="left:521px"></div>

  <div class="foot-col abs" style="left:549px">
    <h3 style="width:66px">Follow Us On</h3>
    <div class="social-row"><span class="social-dot"></span>Friendpage</div>
    <div class="social-row"><span class="social-dot"></span>Chirper</div>
    <div class="social-row"><span class="social-dot"></span>Linkwork</div>
  </div>

  <div class="footer-bar abs">Copyright © 2016 ThornwickEstateManagementLtd. All Rghts Reserved.</div>
</footer>

</body>
</html>
```